Flyer-Design für Vertrieb von LED-Beleuchtung
Zielgruppe
Vertrieb von Led Beleuchtung,, für Biergärten
Shop-Adresse lautet www.brilo-nox-markt.de diese sollte auch unbedingt mit rein!
Aufgabenstellung
Es geht Hauptsächlich nur um Bunte Led Birnen und die dazugehörigen Fassungen.
Daher bitte eigene Bilder benutzen und zusätzlich noch welche suchen die passen würden.
Aussagen soll es wie sehr man durch die Umstellung auf unsere Birnen sparen kann und dass sie besser Leuchten als normale und nicht kaputt gehen. 2 alte Flyerversuche von mir selbst liegen bei zwecks preise etc. Die Antwortkarte darf nicht mehr drauf sein da dies bereits Formatprobleme mit der Post gab

```html
<!DOCTYPE html>
<html lang="de">
<head>
<meta charset="utf-8">
<title>Lumvaro – Stromsparende LED Beleuchtung</title>
<link rel="stylesheet" href="https://fonts.googleapis.com/css2?family=Bodoni+Moda:wght@400&family=Open+Sans:wght@400;700&display=swap">
<style>
  :root {
    --bg: #050608;
    --yellow: #ffe600;
    --white: #ffffff;
    --photo-dark: #03050b;
    --photo-blue: #1d3b66;
    --photo-red: #5a1420;
  }
  html, body {
    margin: 0;
    padding: 0;
    overflow: hidden;
    background: var(--bg);
  }
  .flyer {
    position: relative;
    width: 1200px;
    height: 848px;
    background: var(--bg);
    overflow: hidden;
    font-family: "Open Sans", Arial, sans-serif;
    color: var(--white);
  }
  .serif {
    font-family: "Bodoni Moda", "Times New Roman", serif;
    font-weight: 400;
    color: var(--yellow);
  }
  .panel-back {
    position: absolute;
    left: 20px;
    top: 288px;
    width: 400px;
    text-align: center;
  }
  .panel-back__headline {
    margin: 0;
    font-size: 34px;
    line-height: 46px;
  }
  .panel-back__text {
    margin: 12px 0 0;
    font-size: 14px;
    line-height: 17px;
  }
  .panel-back__claims {
    margin: 10px 0 0;
    font-size: 14px;
    line-height: 17px;
    color: var(--yellow);
  }
  .contact {
    position: absolute;
    left: 464px;
    top: 414px;
    font-size: 16.5px;
    line-height: 20.5px;
  }
  .contact p {
    margin: 0 0 20.5px;
  }
  .cover-photo {
    position: absolute;
    left: 841px;
    top: 113px;
    width: 274px;
    height: 114px;
    background:
      radial-gradient(ellipse at 25% 75%, var(--photo-red) 0%, transparent 35%),
      radial-gradient(ellipse at 65% 65%, var(--photo-blue) 0%, transparent 45%),
      var(--photo-dark);
  }
  .cover-headline {
    position: absolute;
    left: 838px;
    top: 260px;
    margin: 0;
    width: 350px;
    font-size: 46px;
    line-height: 64px;
  }
  .brand {
    position: absolute;
    left: 839px;
    top: 580px;
  }
  .brand__name {
    margin: 0;
    font-weight: 700;
    font-size: 44px;
    line-height: 46px;
  }
  .brand__tagline {
    margin: 0;
    font-size: 17px;
    line-height: 20px;
  }
</style>
</head>
<body>
  <main class="flyer">
    <section class="panel-back">
      <h2 class="panel-back__headline serif">Damit Sie nicht<br>im Dunkeln sitzen!</h2>
      <p class="panel-back__text">Viel Bewegen durch einfaches Austauschen und<br>Umsteigen auf umweltschonende LED Birnen.</p>
      <p class="panel-back__claims">Bis zu 80 % Strom sparen – heller als normale<br>Birnen und langlebig statt schnell kaputt.</p>
    </section>

    <section class="contact">
      <p>Adresse</p>
      <p>Lumvaro<br>Talmarkstr. 8<br>71904 Rendorf<br>Deutschland</p>
      <p>Ansprechpartner</p>
      <p>Jelu Pandor<br>E-Mail info@vamuro-shop.de<br>Shop www.brilo-nox-markt.de</p>
    </section>

    <div class="cover-photo" role="img" aria-label="Foto: hängende leuchtende LED-Birnen mit roten und blauen Fassungen vor dunklem Hintergrund"></div>

    <h1 class="cover-headline serif">Durch<br>aufleuchtende<br>Momente ins<br>Auge Fallen</h1>

    <div class="brand">
      <p class="brand__name">LUMVARO</p>
      <p class="brand__tagline">Stromsparende LED Beleuchtung</p>
    </div>
  </main>
</body>
</html>
```